Desktop and Mobile Site Homepage Redesign

We need a new website homepage redesign for www.plomzar.com. Plomzar is a new startup company based in San Francisco. We develop innovative iPhone application for consumers.
Our initial product is Plomzar that connects tv audiences with their favorite tv shows and fans. We would like to see designs that use the color red. The final design should communicate fun entertainment with social aspects relevant to USA cable tv shows.

We need 1. Desktop website and 2. Mobile website

Target Market(s)

USA

Industry/Entity Type

Entertainment

Number of Pages Required

2 page

Requirements
Must have
• Company name and logo. 1 Page Desktop View and 1 Page Mobile View.
Nice to have
• Details visit www.plomzar.com

```html
<!DOCTYPE html>
<html lang="en">
<head>
<meta charset="utf-8">
<title>Plomzar — Social TV App</title>
<link href="https://fonts.googleapis.com/css2?family=Lato:wght@300;400;700;900&display=swap" rel="stylesheet">
<style>
:root{
  --red:#e30613;
  --red-deep:#c4000d;
  --red-soft:#f2415a;
  --ink:#222;
  --grey-text:#666;
  --topbar:#5b5b5b;
  --light:#f1f1f1;
  --navy:#13202b;
  --white:#fff;
}
*{margin:0;padding:0;box-sizing:border-box}
html,body{width:1200px;height:3782px;overflow:hidden}
body{font-family:'Lato',Arial,sans-serif;color:var(--ink);background:var(--white);position:relative}
.abs{position:absolute}
.ph{position:absolute}

/* top bar */
.topbar{left:0;top:0;width:1200px;height:35px;background:var(--topbar);color:#eee;font-size:12px}
.topbar .item{position:absolute;top:10px;display:flex;align-items:center;gap:6px}
.topbar .social{position:absolute;right:146px;top:8px;display:flex;gap:8px}
.topbar .social span{width:19px;height:19px;border-radius:50%;background:#eee;display:block}

/* header */
.header{left:0;top:35px;width:1200px;height:111px;background:var(--white)}
.brand{position:absolute;left:146px;top:28px;display:flex;align-items:center;gap:10px;color:var(--red);font-weight:700;font-size:34px}
.brand .dot{width:26px;height:26px;border-radius:50%;background:var(--red)}
.promo{position:absolute;left:446px;top:28px;width:688px;height:58px;border-radius:29px;background:var(--red);color:var(--white);display:flex;align-items:center;padding-left:34px}
.promo strong{font-weight:400;font-size:34px;letter-spacing:1px}
.promo em{font-style:normal;font-size:21px;margin-left:12px;opacity:.9}
.promo .pill{position:absolute;right:14px;top:9px;width:214px;height:40px;border-radius:20px;background:var(--white);color:var(--red);font-weight:900;font-size:17px;display:flex;align-items:center;justify-content:center;letter-spacing:1px}

/* hero */
.hero{left:0;top:146px;width:1200px;height:471px;background:linear-gradient(135deg,var(--red-deep) 0%,var(--red) 50%,#d8000e 100%)}
.hero h1{position:absolute;left:150px;top:120px;color:var(--white);font-weight:300;line-height:1}
.hero h1 .a{display:block;font-weight:900;font-size:72px}
.hero h1 .b{display:block;font-size:66px;margin-top:6px}
.hero h1 .c{display:block;font-weight:900;font-size:50px;margin-top:12px}
.app-shot{left:796px;top:166px;width:248px;height:514px;background:linear-gradient(180deg,#3c3f6e 0%,#8b8fa6 45%,#e4e4e8 100%)}

/* sport */
.sport{left:0;top:617px;width:1200px;height:567px;background:radial-gradient(ellipse at 50% 40%,#ffffff 0%,var(--light) 70%,#e6e6e6 100%)}
.frame{left:151px;top:713px;width:487px;height:363px;background:var(--white);border:1px solid #ddd;padding:14px}
.frame .ph{position:relative;width:100%;height:100%;background:linear-gradient(135deg,#5a6a74,#c9c4bb 60%,#8f8a82)}
.sport-copy{left:662px;top:770px;width:420px}
.kicker{color:var(--red);font-weight:700;font-size:44px;line-height:1}
.thin{font-weight:300;font-size:48px;color:var(--ink);line-height:1.05}
.rule{height:1px;background:#bbb;margin:20px 0 18px}
.sub{font-size:24px;color:var(--grey-text)}
.btn{display:inline-flex;align-items:center;justify-content:center;background:var(--red);color:var(--white);font-weight:700;font-size:12px;border-radius:20px;letter-spacing:.5px}
.sport-copy .btn{width:124px;height:40px;margin-top:38px}

/* reality */
.reality{left:0;top:1184px;width:1200px;height:580px;background:linear-gradient(180deg,var(--red) 0%,var(--red-soft) 28%,#f7a6b3 48%,#fde6ea 62%,#fff 76%)}
.reality h2{position:absolute;top:68px;width:100%;text-align:center;color:var(--white);font-weight:900;font-size:54px}
.reality .lead{position:absolute;top:138px;width:100%;text-align:center;color:#222;font-size:22px}
.tv-shot{left:383px;top:1386px;width:436px;height:290px;background:linear-gradient(135deg,#3a2a5c,#8a4a9a 50%,#2c2240)}
.reality .note{position:absolute;top:530px;width:100%;text-align:center;font-size:22px;font-weight:700;color:#222}

/* search & follow */
.follow-head{left:0;top:1818px;width:1200px;text-align:center}
.follow-head h2{font-weight:300;font-size:46px;display:flex;align-items:center;justify-content:center;gap:26px}
.follow-head h2::before,.follow-head h2::after{content:"";width:150px;height:1px;background:#888}
.follow-head p{font-size:19px;color:var(--grey-text);margin-top:12px}
.card{top:1976px;width:444px}
.card .ph{position:relative;width:444px;height:272px}
.card h3{color:var(--red);font-weight:900;font-size:34px;margin:26px 0 0 18px}
.card .line2{font-weight:300;font-size:38px;margin-left:18px;line-height:1.2}
.card .rule{margin:10px 0 14px 18px}
.card p{font-size:16px;color:#333;margin-left:18px}
.card .btn{width:96px;height:30px;font-size:10px;margin:24px 0 0 18px}

/* split blocks */
.redbox{background:var(--red);color:var(--white)}
.share{left:146px;top:2543px;width:373px;height:355px;padding:52px 0 0 28px}
.share .k{font-weight:300;font-size:24px}
.share .big{font-weight:900;font-size:48px;line-height:1.15;margin-top:10px}
.share .s{font-size:21px;margin-top:8px}
.share-photo{left:519px;top:2543px;width:681px;height:355px;background:linear-gradient(120deg,#d9d2c4,#9aa7a9 45%,#6d7a78)}
.talk-photo{left:0;top:2898px;width:683px;height:353px;background:linear-gradient(120deg,#8a6e5c,#d8c6b0 50%,#a6705f)}
.talk{left:683px;top:2898px;width:368px;height:353px;padding:56px 0 0 24px}
.talk .k{font-weight:300;font-size:24px}
.talk .big{font-weight:900;font-size:48px;line-height:1.2;margin-top:10px}
.talk .s{font-size:19px;margin-top:8px}

/* contact */
.contact{left:0;top:3251px;width:1200px;height:474px;background:radial-gradient(ellipse at 70% 40%,#2c3b47 0%,var(--navy) 60%,#0a1117 100%)}
.contact h2{position:absolute;top:60px;width:100%;text-align:center;color:var(--white);font-weight:700;font-size:40px;letter-spacing:1px}
.field{position:absolute;border:1px solid #9aa3aa;border-radius:4px;color:#aab;font-size:12px;padding:12px 14px;background:rgba(255,255,255,.03)}
.f-name{left:146px;top:149px;width:449px;height:42px}
.f-mail{left:605px;top:149px;width:448px;height:42px}
.f-subj{left:146px;top:199px;width:907px;height:43px}
.f-subj svg{position:absolute;right:14px;top:16px}
.f-msg{left:146px;top:249px;width:907px;height:124px}
.contact .btn{position:absolute;left:524px;top:391px;width:151px;height:42px;font-size:15px;border-radius:21px}
.footer{left:0;top:3725px;width:1200px;height:57px;background:#e9e9e9;color:#777;font-size:12px;text-align:center;padding-top:21px}
</style>
</head>
<body>

<div class="abs topbar">
  <div class="item" style="left:146px">
    <svg width="12" height="12" viewBox="0 0 12 12"><path d="M2 1h3l1 3-2 1a7 7 0 0 0 3 3l1-2 3 1v3c-6 0-10-4-10-9z" fill="#eee"/></svg>029-5512-730
  </div>
  <div class="item" style="left:285px">
    <svg width="13" height="10" viewBox="0 0 13 10"><rect x=".5" y=".5" width="12" height="9" fill="none" stroke="#eee"/><path d="M.5 .5l6 5 6-5" fill="none" stroke="#eee"/></svg>info@plomzar.com
  </div>
  <div class="item" style="left:420px">
    <svg width="10" height="13" viewBox="0 0 10 13"><path d="M5 0a5 5 0 0 0-5 5c0 4 5 8 5 8s5-4 5-8a5 5 0 0 0-5-5z" fill="#eee"/><circle cx="5" cy="5" r="2" fill="#5b5b5b"/></svg>418 Alder Ave, Fremont, CA 94536
  </div>
  <div class="social"><span></span><span></span><span></span><span></span></div>
</div>

<header class="abs header">
  <div class="brand"><span class="dot"></span>Plomzar</div>
  <div class="promo"><strong>SOCIAL TV APP</strong><em>coming soon</em><span class="pill">SIGN UP</span></div>
</header>

<section class="abs hero">
  <h1><span class="a">TURN ON</span><span class="b">YOUR TV AND JOIN</span><span class="c">THE FANS IN REAL TIME</span></h1>
</section>
<div class="abs app-shot" role="img" aria-label="Photo of a smartphone showing the app's live show chat screen"></div>

<section class="abs sport"></section>
<div class="abs frame"><div class="ph" role="img" aria-label="Photo of a hand holding a phone showing live sports over a laptop"></div></div>
<div class="abs sport-copy">
  <div class="kicker">LIVE SPORT</div>
  <div class="thin">CHATROOMS</div>
  <div class="rule"></div>
  <div class="sub">Follow Your Favorite Sports Teams</div>
  <span class="btn">GET THE APP</span>
</div>

<section class="abs reality">
  <h2>REALITY TV CHATROOMS</h2>
  <p class="lead">Movies, News, Game Shows, And Everything On TV</p>
  <p class="note">Don't Miss Your TV Shows Get Automatic Reminders</p>
</section>
<div class="abs tv-shot" role="img" aria-label="Photo of a television showing a performer on a colourful stage"></div>

<div class="abs follow-head">
  <h2>SEARCH AND FOLLOW</h2>
  <p>Sort Your TV Channels And Much More...</p>
</div>

<div class="abs card" style="left:146px">
  <div class="ph" role="img" aria-label="Photo of a young man with headphones looking at his phone by the water" style="background:linear-gradient(135deg,#b9c6cc,#7d8d94 55%,#3f4a4f)"></div>
  <h3>The Best TV Guide App</h3>
  <div class="line2">Connect Instantly</div>
  <div class="rule"></div>
  <p>Can't Wait For Your Friends To Comment Back?</p>
  <span class="btn">GET THE APP</span>
</div>
<div class="abs card" style="left:610px">
  <div class="ph" role="img" aria-label="Photo of three friends at a café table looking at a phone" style="background:linear-gradient(135deg,#ede6da,#c9b8a3 55%,#6f6358)"></div>
  <h3>Social TV Guide</h3>
  <div class="line2">Live Chat With Real Fans</div>
  <div class="rule"></div>
  <p>Live, Laugh and Connect</p>
  <span class="btn">GET THE APP</span>
</div>

<div class="abs redbox share">
  <div class="k">FOLLOW YOUR FRIENDS</div>
  <div class="big">SHARE<br>AND<br>INVITE</div>
  <div class="s">Your Friends To Any TV Show</div>
</div>
<div class="abs share-photo" role="img" aria-label="Photo of a group of friends outdoors looking at their phones"></div>

<div class="abs talk-photo" role="img" aria-label="Photo of excited friends cheering on a sofa in front of the TV"></div>
<div class="abs redbox talk">
  <div class="k">TALK ABOUT TV</div>
  <div class="big">ALL NEW<br>TV GUIDE<br>APP</div>
  <div class="s">Coming Soon</div>
</div>

<section class="abs contact">
  <h2>GET IN TOUCH</h2>
  <div class="field f-name">Your Name</div>
  <div class="field f-mail">Your Email</div>
  <div class="field f-subj">Your Subject
    <svg width="12" height="8" viewBox="0 0 12 8"><path d="M0 0h12L6 8z" fill="#dfe3e6"/></svg>
  </div>
  <div class="field f-msg">Your Message</div>
  <span class="btn">SIGN UP</span>
</section>

<footer class="abs footer">Copyright 2017 Plomzar, Inc.</footer>

</body>
</html>
```